VarloPeak

Need a 6 page template designed in Layered PSD for a house cleaning company.

Target Market(s)

People who are selling their homes and need house cleaning

Industry/Entity Type

House cleaning

Number of Pages Required

5+ page

Font styles to use
Sans Serif

Requirements
Must have
• Please see the zip file included with the brief. It has a document with detailed instructions.

```html
<!DOCTYPE html>
<html lang="en">
<head>
<meta charset="utf-8">
<title>VarloPeak — Deep Pre-Sale, Move-In &amp; Move-Out Cleaning</title>
<link href="https://fonts.googleapis.com/css2?family=Libre+Baskerville:wght@400;700&family=Roboto:wght@400;500;700&display=swap" rel="stylesheet">
<style>
:root{
  --navy:#233a8b;
  --navy-deep:#1c2f74;
  --green:#5cb135;
  --ink:#2a2a2a;
  --muted:#8a8a8a;
  --light:#eff0f2;
  --footer:#2d2d2f;
  --white:#ffffff;
}
*{margin:0;padding:0;box-sizing:border-box}
html,body{width:1200px;height:4878px;overflow:hidden;background:var(--white)}
body{font-family:"Roboto",Arial,sans-serif;color:var(--ink);position:relative}
.serif{font-family:"Libre Baskerville",Georgia,serif;font-weight:700;text-transform:uppercase}
section,header,footer{position:absolute;left:0;width:1200px}
.btn{position:absolute;display:flex;align-items:center;justify-content:center;border-radius:24px;font-size:14px;font-weight:700;text-transform:uppercase;color:var(--white);background:var(--green)}
.placeholder{position:absolute}

/* header */
.site-header{top:0;height:95px;background:var(--white)}
.brand{position:absolute;left:112px;top:30px;display:flex;align-items:center;gap:10px;font-size:30px;font-weight:700;color:var(--navy)}
.brand .mark{width:16px;height:16px;background:var(--green);border-radius:50%}
.nav a{position:absolute;top:36px;font-size:15px;color:#333;text-decoration:none;text-transform:uppercase}
.nav a.active{color:var(--green)}
.contact-btn{left:939px;top:23px;width:153px;height:44px;font-size:15px}

/* hero */
.hero{top:95px;height:562px}
.hero h1{position:absolute;left:112px;top:116px;font-size:23px;line-height:39px;color:var(--white);white-space:nowrap}
.hero .rule{position:absolute;left:112px;top:290px;width:75px;height:3px;background:var(--green)}
.hero p{position:absolute;left:112px;top:313px;width:500px;font-size:16px;line-height:27px;color:var(--white)}
.hero .btn{left:112px;top:397px;width:157px;height:45px}

/* pre-sale */
.presale{top:657px;height:536px}
.presale .frame{position:absolute;left:117px;top:91px;width:430px;height:399px;border:2px solid var(--green);border-radius:18px}
.presale h2{position:absolute;left:615px;top:78px;white-space:nowrap;font-size:26px;line-height:44px;color:var(--navy)}
.presale p{position:absolute;left:615px;top:222px;width:475px;font-size:14.5px;line-height:26px;text-align:justify}
.presale .btn{left:615px;top:445px;width:159px;height:47px}

.section-title{position:absolute;left:0;width:1200px;text-align:center;font-size:27px;color:var(--navy)}
.services-title{top:1228px}
.tiles{top:1302px;height:364px}
.tile{position:absolute;top:0;width:297px;height:364px}
.tile span{position:absolute;left:0;right:0;bottom:46px;text-align:center;color:var(--white);font-weight:700;font-size:19px;text-transform:uppercase}

/* move in */
.movein h2{position:absolute;left:0;top:1752px;width:1200px;text-align:center;font-size:27px;line-height:43px;color:var(--navy);white-space:nowrap}
.movein p{position:absolute;left:150px;top:1898px;width:900px;text-align:center;font-size:14.5px;line-height:26px}
.realtors h3{position:absolute;left:112px;top:2066px;font-size:29px;color:var(--green)}
.realtors p{position:absolute;left:112px;top:2120px;width:428px;font-size:14.5px;line-height:25.7px;text-align:justify}
.realtors .btn{left:112px;top:2355px;width:238px;height:46px;background:var(--navy);font-size:13px}

/* move out */
.moveout{top:2540px;height:839px}
.moveout h2{position:absolute;left:0;top:76px;width:1200px;text-align:center;font-size:27px;line-height:43px;color:var(--white);white-space:nowrap}
.moveout .lede{position:absolute;left:150px;top:196px;width:900px;text-align:center;font-size:14px;line-height:25px;color:var(--white)}
.card{position:absolute;top:341px;width:308px;height:428px;background:var(--white);border-radius:14px;text-align:center}
.card.featured{background:var(--green);top:336px;height:440px}
.card .icon{width:112px;height:112px;border-radius:50%;margin:18px auto 0;border:2px solid #c9e6b9;display:flex;align-items:center;justify-content:center}
.card.featured .icon{border-color:var(--white)}
.card h4{margin-top:20px;font-size:17px;line-height:26px;text-transform:uppercase;color:#222;font-weight:700}
.card.featured h4,.card.featured p{color:var(--white)}
.card p{margin:14px 14px 0;font-size:12px;line-height:23px;color:var(--muted)}

/* speciality */
.specialty h2{position:absolute;left:589px;top:3490px;white-space:nowrap;font-size:27px;line-height:41px;color:var(--navy)}
.specialty p{position:absolute;left:589px;top:3720px;width:495px;font-size:14.5px;line-height:26px;text-align:justify}

/* areas */
.areas{top:3975px;height:468px;background:var(--light)}
.areas h3{position:absolute;left:640px;top:88px;font-size:27px;color:var(--green)}
.areas ul{position:absolute;top:145px;list-style:none;font-size:17px;line-height:27.5px;color:#333}
.areas li::before{content:"•";position:absolute;left:-30px;color:#555}
.areas li{position:relative}

/* footer */
.site-footer{top:4443px;height:435px;background:var(--footer);color:var(--white)}
.footer-brand{position:absolute;left:112px;top:110px;display:flex;align-items:center;gap:12px;font-size:38px;font-weight:700}
.footer-brand .mark{width:18px;height:18px;background:var(--green);border-radius:50%}
.fcol{position:absolute;top:82px;font-size:14.5px}
.fcol h5{font-size:16px;font-weight:700;text-transform:uppercase;margin-bottom:14px}
.fcol li{list-style:none;line-height:39px}
.contact-item{position:relative;padding-left:34px;margin-bottom:18px;line-height:19px}
.contact-item b{display:block;font-size:14.5px}
.contact-item svg{position:absolute;left:0;top:2px}
.footer-rule{position:absolute;left:112px;top:375px;width:976px;height:1px;background:#4a4a4c}
.copyright{position:absolute;left:0;top:396px;width:1200px;text-align:center;font-size:13px}
</style>
</head>
<body>

<header class="site-header">
  <div class="brand"><span class="mark"></span>VarloPeak</div>
  <nav class="nav">
    <a class="active" style="left:392px">Home</a>
    <a style="left:462px">Services</a>
    <a style="left:558px">What's Included</a>
    <a style="left:715px">For Realtors</a>
    <a style="left:848px">Blog</a>
  </nav>
  <a class="btn contact-btn">Contact Us</a>
</header>

<section class="hero">
  <div class="placeholder" role="img" aria-label="Cleaners at work in a bright home under a deep blue overlay" style="inset:0;background:linear-gradient(120deg,#263f93,#213785 60%,#2a4497)"></div>
  <h1 class="serif">The only Barrie area cleaning<br>service that specializes in deep<br>pre-sale, move-in, &amp; move-out<br>house cleanings</h1>
  <div class="rule"></div>
  <p>Welcome to the only Barrie area cleaning service specializing in deep move-in, move-out, and pre-sale house cleanings.</p>
  <a class="btn">Learn More</a>
</section>

<section class="presale">
  <div class="frame"></div>
  <div class="placeholder" role="img" aria-label="Person mopping a wooden floor beside an orange bucket" style="left:129px;top:90px;width:418px;height:389px;border-radius:16px;background:linear-gradient(160deg,#8a8f8c,#c9b39a 60%,#d9cdbd)"></div>
  <h2 class="serif">Pre-Sale Cleanings: Are<br>you putting your Barrie<br>area home up for sale?</h2>
  <p>First impressions matter, and a clean and fresh home can make a huge difference. At VarloPeak.com, we specialize in deep cleaning services that will get your home in tip-top shape for potential buyers. Not only will a move-out deep cleaning make your home more attractive to potential buyers, but it can also increase its value. A well-maintained home is a valuable asset that can command a higher price on the Barrie area market.</p>
  <a class="btn">Learn More</a>
</section>

<h2 class="section-title serif services-title">Cleaning Services We Offer</h2>
<section class="tiles">
  <div class="tile" role="img" aria-label="Cleaner vacuuming a tiled hallway, green tint" style="left:0;background:linear-gradient(180deg,#7d9e78,#6b9a62)"><span>Pre-Sale Cleaning</span></div>
  <div class="tile" role="img" aria-label="Couple carrying a sofa into a new home, blue tint" style="left:300px;background:linear-gradient(180deg,#8aa0b9,#6f8cac)"><span>Move-In Cleaning</span></div>
  <div class="tile" role="img" aria-label="Couple packing cardboard boxes, green tint" style="left:600px;background:linear-gradient(180deg,#a7b590,#8aa56f)"><span>Move-Out Cleaning</span></div>
  <div class="tile" role="img" aria-label="Hands filling a blue rubbish bag" style="left:903px;background:linear-gradient(180deg,#4a5d88,#2f55a8)"><span>Junk Removal</span></div>
</section>

<div class="movein">
  <h2 class="serif">Move-In Cleanings: Take the stress out of<br>your move &amp; haveyour home sparkling<br>clean before you move in</h2>
  <p>Moving doesn't have to be a stressful experience. Let us take the hassle out of your move and ensure your new Barrie home is clean, fresh, and ready for you to settle in. Our Barrie area move-in deep cleaning Service is designed so that you can start your new chapter with a spotless and hygienic environment. Our experienced and skilled cleaners will work diligently to ensure that every nook and cranny of your new Barrie home is perfectly cleaned.</p>
</div>

<div class="realtors">
  <h3 class="serif">Attention Realtors</h3>
  <p>As a Barrie area realtor, you know that buying or selling a home can be stressful for your clients. Here at VarloPeak.com, we want to help make that process as smooth as possible. That's why we're excited to introduce our Barrie area move-in &amp; move-out deep cleaning services as a value-added service for your clients.Let us take the hassle out of your client's move and ensure their Barrie home is deep-cleaned, fresh, and ready.</p>
  <a class="btn">Click Here For More Info</a>
  <div class="placeholder" role="img" aria-label="Smiling cleaner holding a bucket of cleaning supplies and yellow gloves" style="left:620px;top:2012px;width:400px;height:528px;background:linear-gradient(180deg,#f1f1f1,#d7dbe6 50%,#3d5a8f);border-radius:200px 200px 0 0"></div>
</div>

<section class="moveout">
  <div class="placeholder" role="img" aria-label="Cleaning team at work under a deep blue overlay" style="inset:0;background:linear-gradient(120deg,#24398a,#213684 50%,#2a4396)"></div>
  <h2 class="serif">Move-Out Cleanings: Cleaned &amp; ready<br>for the next occupants</h2>
  <p class="lede">Looking for a professional move-out cleaning service to ensure that your property is left sparkling clean and ready for the next occupants? Look no further than our expert team of cleaning professionals! At VarloPeak.com, we provide move-out cleaning services to homeowners and tenants throughout the Barrie area. Our team of experienced and fully trained cleaners will work tirelessly to ensure your property is left in pristine condition when you move out so that you can focus on your move without any added stress.</p>

  <div class="card" style="left:112px">
    <div class="icon"><svg width="54" height="54" viewBox="0 0 54 54" fill="none" stroke="#5cb135" stroke-width="2"><path d="M8 26 27 10l19 16"/><path d="M14 22v22h26V22"/><path d="M22 44V32h10v12"/></svg></div>
    <h4>Move-Out Cleaning<br>for Homeowners</h4>
    <p>Move-out cleaning for Barrie area homeowners is a deep cleaning service typically performed when the homeowner prepares to move out. The purpose of move-out cleaning is to leave the property in a sparkling clean condition, ready for the next occupants to move in or for the final inspection by the new homeowner.</p>
  </div>
  <div class="card featured" style="left:445px">
    <div class="icon"><svg width="54" height="54" viewBox="0 0 54 54" fill="none" stroke="#ffffff" stroke-width="2"><path d="M8 26 27 10l19 16"/><path d="M14 22v22h26V22"/><rect x="21" y="28" width="12" height="10"/></svg></div>
    <h4>Move-Out Cleaning<br>for Renters</h4>
    <p>Are you moving out of your Barrie area rental property soon and need to ensure that the property is left clean and in pristine condition to get your security deposit back? Don't let the stress of move-out cleaning get in the way of getting your security deposit back. Contact us today to schedule your move-out cleaning service, and let us help you leave your rental in pristine condition when you move out.</p>
  </div>
  <div class="card" style="left:778px">
    <div class="icon"><svg width="54" height="54" viewBox="0 0 54 54" fill="none" stroke="#5cb135" stroke-width="2"><path d="M8 26 27 10l19 16"/><path d="M14 22v22h26V22"/><path d="M20 44V34h14v10"/><path d="M36 14v-4h5v9"/></svg></div>
    <h4>Move Out Cleaning for<br>Landlords &amp; Property</h4>
    <p>Move-out cleaning for Barrie area landlords &amp; property managers is a deep cleaning service typically performed when a tenant vacates the rental property. This deep cleaning is critical in ensuring that rental properties are in good condition, ready for new tenants, and preventing any delays in the turnover process.</p>
  </div>
</section>

<div class="specialty">
  <div class="placeholder" role="img" aria-label="Two masked cleaners in aprons holding spray bottles, in a circular frame" style="left:102px;top:3466px;width:440px;height:440px;border-radius:50%;background:radial-gradient(circle at 60% 35%,#8fb98a,#4a5e55 70%,#2f3a3a)"></div>
  <h2 class="serif">The only Barrie area<br>cleaningservice that<br>specializes in deep&nbsp; pre-sale,<br>move-in &amp; move-out house<br>cleanings</h2>
  <p>Whether you're moving into or out of a Barrie area home, apartment, or rental property, our Barrie area Pre-Sale, Move-In, and Move-Out Deep Cleaning Services are the perfect solution for you. Contact us today to schedule an appointment, and let us take care of the daunting task of having your home deep cleaned so that you can enjoy your new Barrie area home from day one.</p>
</div>

<section class="areas">
  <div class="placeholder" role="img" aria-label="Grey world map with red location pins" style="left:72px;top:95px;width:496px;height:303px;border-radius:40px;background:radial-gradient(ellipse at center,#8a8a8a,#a9a9a9 60%,#eff0f2 90%)"></div>
  <h3 class="serif">Areas We Service</h3>
  <ul style="left:666px">
    <li>Barrie</li><li>Innisfil</li><li>Springwater</li><li>Minesing</li><li>Orillia</li><li>Wasaga</li><li>Midland</li><li>Angus</li><li>Collingwood</li>
  </ul>
  <ul style="left:867px">
    <li>New Lowell</li><li>Oro-Medonte</li><li>Shanty Bay</li><li>Horseshoe Valley</li><li>Coldwater</li><li>Stayner</li><li>Creemore</li><li>Alliston</li><li>And everywhere in between</li>
  </ul>
</section>

<footer class="site-footer">
  <div class="footer-brand"><span class="mark"></span>VarloPeak</div>
  <div class="fcol" style="left:415px">
    <h5>Availability</h5>
    <ul>
      <li style="font-weight:700;font-size:13.5px;text-transform:uppercase">Opening Hours:</li>
      <li>Open 7 Days a Week</li><li>(Monday-Sunday)</li><li>Hours 8:00 am – 9:00 pm</li><li>Evenings &amp; Weekends (Yes)</li><li>Short Notice (Yes)</li>
    </ul>
  </div>
  <div class="fcol" style="left:668px">
    <h5>Quick Links</h5>
    <ul><li>Home</li><li>Services</li><li>What's Included</li><li>For Realtors</li><li>Blog</li></ul>
  </div>
  <div class="fcol" style="left:884px">
    <h5>Contact Info</h5>
    <div class="contact-item"><svg width="12" height="16" viewBox="0 0 12 16"><path d="M6 0a6 6 0 0 0-6 6c0 4.5 6 10 6 10s6-5.5 6-10a6 6 0 0 0-6-6zm0 8.5A2.5 2.5 0 1 1 6 3.5a2.5 2.5 0 0 1 0 5z" fill="#5cb135"/></svg><b>ADDRESS:</b>327, Lorum Ipsum Dolorei,<br>United States.</div>
    <div class="contact-item"><svg width="14" height="14" viewBox="0 0 24 24"><path d="M6.6 10.8a15.1 15.1 0 0 0 6.6 6.6l2.2-2.2a1 1 0 0 1 1-.25 11.4 11.4 0 0 0 3.6.57 1 1 0 0 1 1 1V20a1 1 0 0 1-1 1A17 17 0 0 1 3 4a1 1 0 0 1 1-1h3.5a1 1 0 0 1 1 1c0 1.25.2 2.45.57 3.57a1 1 0 0 1-.25 1z" fill="#5cb135"/></svg><b>PHONE:</b>+1 (888) 888 8888</div>
    <div class="contact-item"><svg width="15" height="12" viewBox="0 0 15 12"><rect width="15" height="12" rx="1" fill="#5cb135"/><path d="M1 1l6.5 5L14 1" stroke="#2d2d2f" stroke-width="1.3" fill="none"/></svg><b>EMAIL:</b>info@VarloPeak.com</div>
  </div>
  <div class="footer-rule"></div>
  <p class="copyright">© 2023 VARLOPEAK &nbsp;|&nbsp; All Rights Reserved</p>
</footer>

</body>
</html>
```